PowerPoint design MervoSan

We need a PowerPoint set-up based upon our existing logo (see joint file)
Our company is operating in the health care and life science sector. We are mainly focussing on international business

Target Market(s)

International

Industry/Entity Type

health care and life sciences

Requirements
Must have
• Logos as added

```html
<!DOCTYPE html>
<html lang="en">
<head>
<meta charset="utf-8">
<title>MervoSan – Presentation Template</title>
<link href="https://fonts.googleapis.com/css2?family=Ubuntu:wght@400;500;700&display=swap" rel="stylesheet">
<style>
  :root{
    --navy:#0b4a8b;
    --navy-dark:#083b70;
    --green:#5cbf14;
    --grey:#4a4a4a;
    --grey-mid:#8a8a8a;
    --grey-light:#f2f2f2;
    --sheet:#c6c6c8;
    --stage:#dfe1e6;
    --white:#ffffff;
    --photo-a:#cfe3e6;
    --photo-b:#8fb7bf;
  }
  *{box-sizing:border-box;margin:0;padding:0}
  html,body{width:1200px;height:3125px;overflow:hidden}
  body{background:var(--sheet);font-family:"Ubuntu",sans-serif;color:var(--grey);position:relative}

  .stage{position:absolute;left:0;top:0;width:1200px;height:728px;background:linear-gradient(180deg,var(--stage),#cfd1d6)}
  .stage-brand{position:absolute;left:884px;top:82px}
  .stage-brand .brand-dot{width:56px;height:56px}
  .stage-brand .brand-name{font-size:36px}
  .hero{position:absolute;left:150px;top:170px;transform:scale(1.3);transform-origin:0 0;box-shadow:0 18px 40px rgba(0,0,0,.25)}

  .slide{position:absolute;width:563px;height:316px;overflow:hidden;background:var(--white)}
  .col-l{left:28px}.col-r{left:609px}.col-c{left:318px}

  .brand{position:absolute;display:flex;align-items:center;gap:8px}
  .brand-dot{width:38px;height:38px;border-radius:50%;background:var(--navy)}
  .brand-name{font-size:23px;font-weight:500;color:var(--navy);letter-spacing:.2px}
  .on-blue .brand-dot{background:var(--white)}
  .on-blue .brand-name{color:var(--white)}

  /* cover slides */
  .cover.on-blue{background:var(--navy)}
  .cover .brand{left:43px;top:52px}
  .cover-title{position:absolute;left:43px;top:122px;font-size:29px;font-weight:500;line-height:1.02;color:var(--navy)}
  .on-blue .cover-title{color:var(--white)}
  .cover-sub{position:absolute;left:43px;top:189px;font-size:11.5px;color:var(--green)}
  .cover-date{position:absolute;left:43px;top:228px;width:126px;height:18px;border-radius:2px;background:var(--navy);color:var(--white);font-size:7px;display:flex;align-items:center;justify-content:center}
  .on-blue .cover-date{background:var(--green)}
  .photo-ring{position:absolute;left:297px;top:-116px;width:400px;height:400px;border-radius:50%;border:10px solid var(--navy);background:linear-gradient(135deg,var(--photo-a),var(--photo-b) 60%,#5b7f8c)}
  .on-blue .photo-ring{border-color:var(--white)}
  .photo-ring.pharmacy{background:linear-gradient(135deg,#e9ecef,#c2c9d3 55%,#8fa0b6)}
  .green-arc{position:absolute;left:287px;top:-126px;width:420px;height:420px;border-radius:50%;border:9px solid transparent;border-bottom-color:var(--green);transform:rotate(-38deg)}
  .ring-dot{position:absolute;left:420px;top:258px;width:24px;height:24px;border-radius:50%;background:var(--green);border:3px solid var(--white)}
  .cover-foot{position:absolute;left:0;bottom:0;width:100%;height:17px;background:var(--grey-light);font-size:6.5px;color:var(--grey-mid);display:flex;align-items:center;justify-content:center;z-index:3}

  /* content footer */
  .foot-brand{position:absolute;left:12px;bottom:10px;gap:4px}
  .foot-brand .brand-dot{width:18px;height:18px}
  .foot-brand .brand-name{font-size:11px}
  .foot-bar{position:absolute;left:100px;right:14px;bottom:15px;height:8px;border-radius:4px;background:linear-gradient(90deg,var(--navy),var(--green));color:var(--white);font-size:4.5px;display:flex;align-items:center;justify-content:flex-end;padding-right:44px}
  .page-no{position:absolute;right:16px;bottom:9px;width:20px;height:20px;background:var(--white);border:2px solid var(--navy);transform:rotate(45deg);display:flex;align-items:center;justify-content:center}
  .page-no span{transform:rotate(-45deg);font-size:6.5px;color:var(--navy);font-weight:700}

  .slide-title{position:absolute;font-size:21px;font-weight:400;color:var(--grey);line-height:1.08}
  .center-title{left:0;width:100%;text-align:center;top:18px}
  .lead{position:absolute;font-size:8px;font-weight:700;color:var(--navy);line-height:1.2}
  .body{position:absolute;font-size:6.3px;color:var(--grey-mid);line-height:1.3}
  .body p{margin-bottom:5px}
  .photo{position:absolute;background:linear-gradient(135deg,var(--photo-a),var(--photo-b))}

  /* slide 5 */
  .s5 .photo{left:23px;top:0;width:207px;height:262px;background:linear-gradient(160deg,#9ec9d2,#e8f0f1 60%,#c9d7da)}
  .s5 .slide-title{left:258px;top:36px}
  .s5 .lead{left:258px;top:80px;width:270px}
  .s5 .body{left:258px;top:112px;width:270px}

  /* slide 6 */
  .s6 .band{position:absolute;left:393px;top:0;width:170px;height:100%;background:var(--navy)}
  .s6 .photo{left:254px;top:30px;width:276px;height:225px;border:3px solid var(--white);background:linear-gradient(135deg,#dfe6ea,#9fb2c2 55%,#4d6c8c)}
  .s6 .slide-title{left:34px;top:30px}
  .s6 .lead{left:34px;top:100px;width:200px}
  .s6 .body{left:34px;top:142px;width:200px}
  .s6 .body li{margin:0 0 5px 10px}
  .s6 .body li::marker{color:var(--navy)}

  /* slide 7 */
  .s7 .band{position:absolute;left:0;top:0;width:100%;height:120px;background:linear-gradient(90deg,#2e8a8c,#4ea56a 55%,#6cbf3a)}
  .s7 .slide-title{color:var(--white);top:20px}
  .member{position:absolute;top:68px;width:160px;text-align:center}
  .member .portrait{width:80px;height:98px;margin:0 auto;background:linear-gradient(180deg,#eceeef,#c9ccd0)}
  .member h3{font-size:11.5px;font-weight:500;margin-top:10px}
  .member .job{font-size:7px;color:var(--grey-mid);margin-top:2px}
  .member .body{position:static;margin-top:8px;padding:0 14px}
  .c-navy{color:var(--navy)}.c-green{color:var(--green)}.c-grey{color:var(--grey)}

  /* slide 8 */
  .feature{position:absolute;width:150px}
  .feature h4{font-size:10.5px;font-weight:400}
  .feature .body{position:static;margin-top:2px}
  .feature.left{left:62px;text-align:right}
  .feature.right{left:352px}
  .icon{position:absolute;width:38px;height:38px;border-radius:50%;display:flex;align-items:center;justify-content:center}
  .bg-navy{background:var(--navy)}.bg-green{background:var(--green)}.bg-grey{background:var(--grey)}

  /* slide 9 */
  .s9{background:linear-gradient(120deg,#b7d8dc,#e6eff0 55%,#c7d9dc)}
  .s9 .photo-label{position:absolute;inset:0}
  .section-ring{position:absolute;left:34px;top:34px;width:242px;height:242px;border-radius:50%;background:var(--white);border:9px solid var(--navy);border-top-color:var(--green);border-right-color:var(--green);transform:rotate(10deg)}
  .section-text{position:absolute;left:34px;top:34px;width:242px;height:242px;display:flex;flex-direction:column;align-items:center;justify-content:center;text-align:center}
  .section-text h2{font-size:26px;font-weight:500;color:var(--navy);line-height:1.05}
  .section-text p{font-size:10px;color:var(--green);margin-top:6px}
  .dot{position:absolute;width:20px;height:20px;border-radius:50%;border:3px solid var(--white)}

  /* slide 10 */
  .gauge{position:absolute;top:80px;width:130px;text-align:center}
  .gauge h4{font-size:13px;font-weight:400;margin-top:8px}
  .gauge .body{position:static;padding:0 10px;margin-top:2px}

  /* slide 11 */
  .s11 .chart{position:absolute;left:36px;top:56px}
  .s11 .body.note{left:48px;top:218px;width:270px}
  .legend{position:absolute;left:358px;width:160px}
  .legend h4{font-size:8px;font-weight:500;display:flex;align-items:center;gap:6px}
  .legend h4 i{display:inline-block;width:11px;height:11px}
  .legend .body{position:static;margin:4px 0 0 20px}

  /* contact slides */
  .contact .photo-quarter{position:absolute;left:-120px;top:-150px;width:300px;height:300px;border-radius:50%;border:7px solid var(--green);border-top-color:var(--white);border-left-color:var(--white);background:linear-gradient(135deg,#dbe3e8,#9fb4c3 60%,#6f8ea6)}
  .contact .brand{left:285px;top:84px}
  .contact .brand .brand-dot{width:30px;height:30px}
  .contact .brand .brand-name{font-size:19px}
  .contact h2{position:absolute;left:285px;top:138px;font-size:14px;font-weight:400;color:var(--grey)}
  .contact .addr{position:absolute;left:285px;top:160px;font-size:7px;color:var(--grey-mid)}
  .contact ul{position:absolute;left:285px;top:180px;list-style:none}
  .contact li{display:flex;align-items:center;gap:7px;font-size:7px;color:var(--grey);height:16px}
  .contact.on-blue{background:var(--navy)}
  .contact.on-blue h2{color:var(--white)}
  .contact.on-blue .addr,.contact.on-blue li{color:var(--white)}
  .contact.on-blue .photo-quarter{border-top-color:var(--navy);border-left-color:var(--navy)}
</style>
</head>
<body>

<section class="stage">
  <div class="brand stage-brand"><span class="brand-dot"></span><span class="brand-name">MervoSan</span></div>

  <article class="slide cover on-blue hero">
    <div class="photo-ring" role="img" aria-label="Photo of a doctor holding a stethoscope"></div>
    <div class="green-arc"></div><div class="ring-dot"></div>
    <div class="brand"><span class="brand-dot"></span><span class="brand-name">MervoSan</span></div>
    <h1 class="cover-title">Presentation<br>Title Goes Here!</h1>
    <p class="cover-sub">Subtitle of Presentation Goes Here!</p>
    <div class="cover-date">Sunday, March 27, 2022</div>
    <footer class="cover-foot">© 2022 MervoSan, All Rights Reserved.</footer>
  </article>
</section>

<!-- Row 1 -->
<article class="slide cover on-blue col-l" style="top:757px">
  <div class="photo-ring" role="img" aria-label="Photo of a doctor holding a stethoscope"></div>
  <div class="green-arc"></div><div class="ring-dot"></div>
  <div class="brand"><span class="brand-dot"></span><span class="brand-name">MervoSan</span></div>
  <h1 class="cover-title">Presentation<br>Title Goes Here!</h1>
  <p class="cover-sub">Subtitle of Presentation Goes Here!</p>
  <div class="cover-date">Sunday, March 27, 2022</div>
  <footer class="cover-foot">© 2022 MervoSan, All Rights Reserved.</footer>
</article>

<article class="slide cover on-blue col-r" style="top:757px">
  <div class="photo-ring pharmacy" role="img" aria-label="Photo of a pharmacist wearing a face mask"></div>
  <div class="green-arc"></div><div class="ring-dot"></div>
  <div class="brand"><span class="brand-dot"></span><span class="brand-name">MervoSan</span></div>
  <h1 class="cover-title">Presentation<br>Title Goes Here!</h1>
  <p class="cover-sub">Subtitle of Presentation Goes Here!</p>
  <div class="cover-date">Sunday, March 27, 2022</div>
  <footer class="cover-foot">© 2022 MervoSan, All Rights Reserved.</footer>
</article>

<!-- Row 2 -->
<article class="slide cover col-l" style="top:1092px">
  <div class="photo-ring" role="img" aria-label="Photo of a doctor holding a stethoscope"></div>
  <div class="green-arc"></div><div class="ring-dot"></div>
  <div class="brand"><span class="brand-dot"></span><span class="brand-name">MervoSan</span></div>
  <h1 class="cover-title">Presentation<br>Title Goes Here!</h1>
  <p class="cover-sub">Subtitle of Presentation Goes Here!</p>
  <div class="cover-date">Sunday, March 27, 2022</div>
  <footer class="cover-foot">© 2022 MervoSan, All Rights Reserved.</footer>
</article>

<article class="slide cover col-r" style="top:1092px">
  <div class="photo-ring pharmacy" role="img" aria-label="Photo of a pharmacist wearing a face mask"></div>
  <div class="green-arc"></div><div class="ring-dot"></div>
  <div class="brand"><span class="brand-dot"></span><span class="brand-name">MervoSan</span></div>
  <h1 class="cover-title">Presentation<br>Title Goes Here!</h1>
  <p class="cover-sub">Subtitle of Presentation Goes Here!</p>
  <div class="cover-date">Sunday, March 27, 2022</div>
  <footer class="cover-foot">© 2022 MervoSan, All Rights Reserved.</footer>
</article>

<!-- Row 3 -->
<article class="slide s5 col-l" style="top:1427px">
  <div class="photo" role="img" aria-label="Photo of a doctor in a white coat with a stethoscope"></div>
  <h2 class="slide-title">Slide Title Goes Here</h2>
  <p class="lead">Our teams support patients and partners across many countries. We share care, research and knowledge to improve health outcomes everywhere.</p>
  <div class="body">
    <p>We work with clinics, hospitals and laboratories to deliver reliable products and services. Every project starts with a clear goal and a plan that our partners can trust from day one.</p>
    <p>Quality and safety guide each step we take. Our experts review every process so that results stay consistent, measurable and easy to follow for all teams.</p>
    <p>We invest in new research and training to keep our people ready for the next challenge in the field.</p>
    <p>Together we build long lasting relations with care providers around the world.</p>
  </div>
  <div class="brand foot-brand"><span class="brand-dot"></span><span class="brand-name">MervoSan</span></div>
  <div class="foot-bar">© 2022 MervoSan, All Rights Reserved.</div>
  <div class="page-no"><span>5</span></div>
</article>

<article class="slide s6 col-r" style="top:1427px">
  <div class="band"></div>
  <div class="photo" role="img" aria-label="Photo of a clinician using a tablet"></div>
  <h2 class="slide-title">Slide Title<br>Goes Here</h2>
  <p class="lead">Our teams support patients and partners across many countries with shared care and clear research goals.</p>
  <ul class="body">
    <li>We work with clinics and laboratories to deliver reliable products and services for every market.</li>
    <li>Quality and safety guide each step. Our experts review every process and result.</li>
    <li>We invest in research and training so our people stay ready. Together we build long lasting relations with care providers and grow our network in every region.</li>
  </ul>
  <div class="brand foot-brand"><span class="brand-dot"></span><span class="brand-name">MervoSan</span></div>
  <div class="foot-bar">© 2022 MervoSan, All Rights Reserved.</div>
  <div class="page-no"><span>6</span></div>
</article>

<!-- Row 4 -->
<article class="slide s7 col-l" style="top:1762px">
  <div class="band" role="img" aria-label="Soft green laboratory background"></div>
  <h2 class="slide-title center-title">Meet our Team</h2>
  <div class="member" style="left:28px">
    <div class="portrait" role="img" aria-label="Team member portrait"></div>
    <h3 class="c-navy">Name Goes Here</h3><p class="job">Job Title Goes Here</p>
    <p class="body">A short note about this person, their role in the team and the work they lead for our partners.</p>
  </div>
  <div class="member" style="left:201px">
    <div class="portrait" role="img" aria-label="Team member portrait"></div>
    <h3 class="c-green">Name Goes Here</h3><p class="job">Job Title Goes Here</p>
    <p class="body">A short note about this person, their role in the team and the work they lead for our partners.</p>
  </div>
  <div class="member" style="left:375px">
    <div class="portrait" role="img" aria-label="Team member portrait"></div>
    <h3 class="c-grey">Name Goes Here</h3><p class="job">Job Title Goes Here</p>
    <p class="body">A short note about this person, their role in the team and the work they lead for our partners.</p>
  </div>
  <div class="brand foot-brand"><span class="brand-dot"></span><span class="brand-name">MervoSan</span></div>
  <div class="foot-bar">© 2022 MervoSan, All Rights Reserved.</div>
  <div class="page-no"><span>7</span></div>
</article>

<article class="slide s8 col-r" style="top:1762px">
  <h2 class="slide-title center-title">Slide Title Goes Here</h2>
  <div class="feature left" style="top:82px"><h4 class="c-navy">Heading Goes Here</h4><p class="body">A short line about this topic and how it helps our partners.</p></div>
  <div class="feature left" style="top:146px"><h4 class="c-grey">Heading Goes Here</h4><p class="body">A short line about this topic and how it helps our partners.</p></div>
  <div class="feature left" style="top:210px"><h4 class="c-green">Heading Goes Here</h4><p class="body">A short line about this topic and how it helps our partners.</p></div>
  <div class="feature right" style="top:82px"><h4 class="c-green">Heading Goes Here</h4><p class="body">A short line about this topic and how it helps our partners.</p></div>
  <div class="feature right" style="top:146px"><h4 class="c-navy">Heading Goes Here</h4><p class="body">A short line about this topic and how it helps our partners.</p></div>
  <div class="feature right" style="top:210px"><h4 class="c-grey">Heading Goes Here</h4><p class="body">A short line about this topic and how it helps our partners.</p></div>

  <div class="icon bg-navy" style="left:227px;top:81px"><svg width="18" height="18" viewBox="0 0 18 18"><circle cx="9" cy="9" r="5" fill="none" stroke="#fff" stroke-width="2"/></svg></div>
  <div class="icon bg-green" style="left:298px;top:81px"><svg width="18" height="18" viewBox="0 0 18 18"><path d="M4 15h10M9 3v9" stroke="#fff" stroke-width="2"/></svg></div>
  <div class="icon bg-grey" style="left:227px;top:146px"><svg width="18" height="18" viewBox="0 0 18 18"><path d="M3 8h12a6 6 0 0 1-12 0z" fill="#fff"/></svg></div>
  <div class="icon bg-navy" style="left:298px;top:146px"><svg width="18" height="18" viewBox="0 0 18 18"><path d="M7 2h4v5l4 8H3l4-8z" fill="#fff"/></svg></div>
  <div class="icon bg-green" style="left:227px;top:209px"><svg width="18" height="18" viewBox="0 0 18 18"><rect x="2" y="5" width="14" height="10" rx="2" fill="#fff"/><path d="M9 7v6M6 10h6" stroke="#5cbf14" stroke-width="2"/></svg></div>
  <div class="icon bg-grey" style="left:298px;top:209px"><svg width="18" height="18" viewBox="0 0 18 18"><path d="M3 15V11h3v4zM8 15V8h3v7zM13 15V4h3v11z" fill="#fff"/></svg></div>

  <div class="brand foot-brand"><span class="brand-dot"></span><span class="brand-name">MervoSan</span></div>
  <div class="foot-bar">© 2022 MervoSan, All Rights Reserved.</div>
  <div class="page-no"><span>8</span></div>
</article>

<!-- Row 5 -->
<article class="slide s9 col-l" style="top:2096px">
  <div class="photo-label" role="img" aria-label="Photo of a doctor holding a stethoscope"></div>
  <div class="section-ring"></div>
  <div class="section-text"><h2>Section Title<br>Goes Here!</h2><p>Subtitle of Section Break</p></div>
  <span class="dot bg-navy" style="left:114px;top:34px"></span>
  <span class="dot bg-green" style="left:118px;top:258px"></span>
</article>

<article class="slide s10 col-r" style="top:2096px">
  <h2 class="slide-title center-title">Slide Title Goes Here</h2>
  <div class="gauge" style="left:54px">
    <svg width="120" height="120" viewBox="0 0 120 120">
      <circle cx="60" cy="60" r="54" fill="none" stroke="#eeeeee" stroke-width="6"/>
      <circle cx="60" cy="60" r="54" fill="none" stroke="var(--navy)" stroke-width="6" stroke-dasharray="217 339" transform="rotate(-90 60 60)"/>
      <text x="60" y="67" text-anchor="middle" font-family="Ubuntu,sans-serif" font-size="22" fill="var(--navy)">64<tspan font-size="11">%</tspan></text>
    </svg>
    <h4 class="c-navy">Heading</h4><p class="body">A short line of text about this figure here.</p>
  </div>
  <div class="gauge" style="left:216px">
    <svg width="120" height="120" viewBox="0 0 120 120">
      <circle cx="60" cy="60" r="54" fill="none" stroke="#eeeeee" stroke-width="6"/>
      <circle cx="60" cy="60" r="54" fill="none" stroke="var(--green)" stroke-width="6" stroke-dasharray="278 339" transform="rotate(-90 60 60)"/>
      <text x="60" y="67" text-anchor="middle" font-family="Ubuntu,sans-serif" font-size="22" fill="var(--green)">82<tspan font-size="11">%</tspan></text>
    </svg>
    <h4 class="c-green">Heading</h4><p class="body">A short line of text about this figure here.</p>
  </div>
  <div class="gauge" style="left:378px">
    <svg width="120" height="120" viewBox="0 0 120 120">
      <circle cx="60" cy="60" r="54" fill="none" stroke="#eeeeee" stroke-width="6"/>
      <circle cx="60" cy="60" r="54" fill="none" stroke="var(--grey)" stroke-width="6" stroke-dasharray="319 339" transform="rotate(-90 60 60)"/>
      <text x="60" y="67" text-anchor="middle" font-family="Ubuntu,sans-serif" font-size="22" fill="var(--grey)">94<tspan font-size="11">%</tspan></text>
    </svg>
    <h4 class="c-grey">Heading</h4><p class="body">A short line of text about this figure here.</p>
  </div>
  <div class="brand foot-brand"><span class="brand-dot"></span><span class="brand-name">MervoSan</span></div>
  <div class="foot-bar">© 2022 MervoSan, All Rights Reserved.</div>
  <div class="page-no"><span>10</span></div>
</article>

<!-- Row 6 -->
<article class="slide s11 col-l" style="top:2431px">
  <h2 class="slide-title center-title">Slide Title Goes Here</h2>
  <svg class="chart" width="290" height="150" viewBox="0 0 290 150" font-family="Ubuntu,sans-serif" font-size="6" fill="#666">
    <g stroke="#ddd" stroke-width=".5">
      <line x1="16" y1="126" x2="285" y2="126"/>
    </g>
    <text x="6" y="128">0</text><text x="6" y="111">1</text><text x="6" y="95">2</text>
    <text x="6" y="78">3</text><text x="6" y="62">4</text><text x="6" y="45">5</text><text x="6" y="29">6</text>
    <g>
      <rect x="30" y="68" width="10" height="58" fill="var(--navy)"/><rect x="42" y="86" width="10" height="40" fill="var(--green)"/><rect x="54" y="93" width="10" height="33" fill="var(--grey)"/>
      <rect x="97" y="85" width="10" height="41" fill="var(--navy)"/><rect x="109" y="54" width="10" height="72" fill="var(--green)"/><rect x="121" y="93" width="10" height="33" fill="var(--grey)"/>
      <rect x="164" y="68" width="10" height="58" fill="var(--navy)"/><rect x="176" y="97" width="10" height="29" fill="var(--green)"/><rect x="188" y="76" width="10" height="50" fill="var(--grey)"/>
      <rect x="231" y="52" width="10" height="74" fill="var(--navy)"/><rect x="243" y="80" width="10" height="46" fill="var(--green)"/><rect x="255" y="43" width="10" height="83" fill="var(--grey)"/>
    </g>
    <text x="36" y="136">Category 1</text><text x="103" y="136">Category 2</text><text x="170" y="136">Category 3</text><text x="237" y="136">Category 4</text>
  </svg>
  <p class="body note">This chart compares results across four groups over the last period. Each bar shows one measure, so teams can see growth, spot gaps and plan the next steps with our partners.</p>
  <div class="legend" style="top:84px"><h4 class="c-navy"><i class="bg-navy"></i>Heading Goes Here</h4><p class="body">A short note that explains what this series means and how it is measured.</p></div>
  <div class="legend" style="top:144px"><h4 class="c-green"><i class="bg-green"></i>Heading Goes Here</h4><p class="body">A short note that explains what this series means and how it is measured.</p></div>
  <div class="legend" style="top:204px"><h4 class="c-grey"><i class="bg-grey"></i>Heading Goes Here</h4><p class="body">A short note that explains what this series means and how it is measured.</p></div>
  <div class="brand foot-brand"><span class="brand-dot"></span><span class="brand-name">MervoSan</span></div>
  <div class="foot-bar">© 2022 MervoSan, All Rights Reserved.</div>
  <div class="page-no"><span>11</span></div>
</article>

<article class="slide contact col-r" style="top:2431px">
  <div class="photo-quarter" role="img" aria-label="Photo of a hand touching a screen"></div>
  <div class="brand"><span class="brand-dot"></span><span class="brand-name">MervoSan</span></div>
  <h2>Contact Us</h2>
  <p class="addr">Insert Company Address Goes Here!</p>
  <ul>
    <li><svg width="9" height="9" viewBox="0 0 10 10"><path d="M2 1l2 2-1 1.5a6 6 0 0 0 2.5 2.5L7 6l2 2-1.5 1.5C4 9 1 6 .5 2.5z" fill="var(--green)"/></svg>Insert Phone Number</li>
    <li><svg width="9" height="9" viewBox="0 0 10 10"><rect x=".5" y="2" width="9" height="6" fill="none" stroke="var(--green)"/><path d="M.5 2l4.5 3.5L9.5 2" fill="none" stroke="var(--green)"/></svg>Insert E-Mail Address</li>
    <li><svg width="9" height="9" viewBox="0 0 10 10"><circle cx="5" cy="5" r="4.3" fill="none" stroke="var(--green)"/><path d="M.7 5h8.6M5 .7c-2 2.5-2 6 0 8.6M5 .7c2 2.5 2 6 0 8.6" fill="none" stroke="var(--green)" stroke-width=".7"/></svg>Insert URL Address</li>
  </ul>
  <footer class="cover-foot">© 2022 MervoSan, All Rights Reserved.</footer>
</article>

<!-- Row 7 -->
<article class="slide contact on-blue col-c" style="top:2766px">
  <div class="photo-quarter" role="img" aria-label="Photo of a hand touching a screen"></div>
  <div class="brand"><span class="brand-dot"></span><span class="brand-name">MervoSan</span></div>
  <h2>Contact Us</h2>
  <p class="addr">Insert Company Address Goes Here!</p>
  <ul>
    <li><svg width="9" height="9" viewBox="0 0 10 10"><path d="M2 1l2 2-1 1.5a6 6 0 0 0 2.5 2.5L7 6l2 2-1.5 1.5C4 9 1 6 .5 2.5z" fill="var(--green)"/></svg>Insert Phone Number</li>
    <li><svg width="9" height="9" viewBox="0 0 10 10"><rect x=".5" y="2" width="9" height="6" fill="none" stroke="var(--green)"/><path d="M.5 2l4.5 3.5L9.5 2" fill="none" stroke="var(--green)"/></svg>Insert E-Mail Address</li>
    <li><svg width="9" height="9" viewBox="0 0 10 10"><circle cx="5" cy="5" r="4.3" fill="none" stroke="var(--green)"/><path d="M.7 5h8.6M5 .7c-2 2.5-2 6 0 8.6M5 .7c2 2.5 2 6 0 8.6" fill="none" stroke="var(--green)" stroke-width=".7"/></svg>Insert URL Address</li>
  </ul>
  <footer class="cover-foot">© 2022 MervoSan, All Rights Reserved.</footer>
</article>

</body>
</html>
```